Lawn mowing business card design

We need a business card design for our lawn mowing and gardening business which is located in the Northern Beaches of Sydney. Our business name is Meadowline Turf and our logo is predominantly green and yellow in color. Please see our website at www.meadowlineturf.com.au for design ideas. The business targets young professionals and older clientele. As such the font should be easy to read, but I also want the business card to be colorful and stand out.

Target Market(s)

young professionals

Industry/Entity Type

Lawn Care

Contact Information for Business Card

Meadowline Turf, Gareth Pellow, 0478559201, www.meadowlineturf.com.au, email: meadowlineturf@mailbox-example.com

Font styles to use
Serif

Colors
9bcb3b
fbed22

Requirements
Must have
• Must include the details listed above. Must include the attached logo.
Nice to have
• Logo attached with two copies. The logo without any writing is high quality, please feel free to be creative with the text stating our business name "Meadowline Turf" using this file.

```html
<!DOCTYPE html>
<html lang="en">
<head>
<meta charset="utf-8">
<title>Meadowline Turf – Business Card</title>
<link rel="stylesheet" href="https://fonts.googleapis.com/css2?family=Noto+Sans:wght@400;700&display=swap">
<style>
  :root {
    --stage: #2b2b2b;
    --lime: #9bcb3b;
    --lime-light: #b5da5a;
    --lime-deep: #86bb2c;
    --field-green: #23843f;
    --field-green-dark: #1d7436;
    --sun-yellow: #fbed22;
    --contact-yellow: #d6e04a;
    --title-green: #7fb83a;
    --paper: #ffffff;
    --paper-shade: #ececec;
    --ink: #1f1f1f;
  }
  * { box-sizing: border-box; margin: 0; padding: 0; }
  html, body {
    width: 1200px;
    height: 900px;
    overflow: hidden;
    background: var(--stage);
    font-family: "Noto Sans", Verdana, sans-serif;
  }
  .canvas {
    position: relative;
    width: 1200px;
    height: 900px;
  }
  .card {
    position: absolute;
    width: 640px;
    height: 366px;
    border-radius: 22px;
    overflow: hidden;
    box-shadow: 0 18px 40px rgba(0,0,0,.45);
  }

  /* Front */
  .card-front {
    left: 60px;
    top: 60px;
    background: radial-gradient(ellipse at 45% 35%, var(--lime-light) 0%, var(--lime) 55%, var(--lime-deep) 100%);
    display: flex;
    align-items: center;
    justify-content: center;
  }
  .brand-mark {
    display: flex;
    align-items: center;
    gap: 16px;
  }
  .brand-dot {
    width: 46px;
    height: 46px;
    border-radius: 50%;
    background: var(--sun-yellow);
  }
  .brand-name {
    font-size: 44px;
    font-weight: 700;
    color: var(--ink);
    letter-spacing: .5px;
  }

  /* Back */
  .card-back {
    left: 500px;
    top: 474px;
    background: linear-gradient(120deg, var(--paper) 0%, var(--paper) 40%, var(--paper-shade) 100%);
  }
  .card-back .wave {
    position: absolute;
    inset: 0;
    width: 100%;
    height: 100%;
  }
  .back-brand {
    position: absolute;
    left: 30px;
    top: 34px;
    font-size: 22px;
    font-weight: 700;
    color: var(--field-green);
  }
  .holder {
    position: absolute;
    left: 34px;
    top: 206px;
  }
  .holder-name {
    font-size: 31px;
    color: var(--sun-yellow);
    line-height: 1.1;
  }
  .holder-title {
    font-size: 17px;
    color: var(--title-green);
    margin-left: 70px;
  }
  .contacts {
    position: absolute;
    right: 26px;
    top: 116px;
    list-style: none;
    text-align: right;
  }
  .contacts li {
    display: flex;
    justify-content: flex-end;
    align-items: center;
    gap: 10px;
    font-size: 15px;
    color: var(--contact-yellow);
    margin-bottom: 13px;
  }
  .contacts svg {
    width: 22px;
    height: 22px;
    flex: none;
  }
</style>
</head>
<body>
<main class="canvas">

  <section class="card card-front" aria-label="Card front">
    <div class="brand-mark">
      <span class="brand-dot"></span>
      <span class="brand-name">Meadowline Turf</span>
    </div>
  </section>

  <section class="card card-back" aria-label="Card back">
    <svg class="wave" viewBox="0 0 640 366" preserveAspectRatio="none" aria-hidden="true">
      <path d="M0 282 C150 290 240 250 330 190 C420 132 520 110 640 104 L640 366 L0 366 Z" fill="var(--field-green)"/>
    </svg>

    <div class="back-brand">Meadowline Turf</div>

    <div class="holder">
      <div class="holder-name">Gareth Pellow</div>
      <div class="holder-title">Title</div>
    </div>

    <ul class="contacts">
      <li>0478559201
        <svg viewBox="0 0 24 24" aria-hidden="true">
          <circle cx="12" cy="12" r="11" fill="var(--contact-yellow)"/>
          <path d="M8.2 6.5l2 2.3-1.2 1.6c.8 1.7 2 2.9 3.6 3.7l1.6-1.2 2.3 2-1.3 1.8c-3.9-.3-8.1-4.5-8.4-8.4z" fill="var(--field-green)"/>
        </svg>
      </li>
      <li>meadowlineturf@mailbox-example.com
        <svg viewBox="0 0 24 24" aria-hidden="true">
          <rect x="2" y="5" width="20" height="14" fill="none" stroke="var(--contact-yellow)" stroke-width="2"/>
          <path d="M2 5l10 8 10-8" fill="none" stroke="var(--contact-yellow)" stroke-width="2"/>
        </svg>
      </li>
      <li>www.meadowlineturf.com.au
        <svg viewBox="0 0 24 24" aria-hidden="true">
          <circle cx="12" cy="12" r="11" fill="var(--contact-yellow)"/>
          <g fill="none" stroke="var(--field-green)" stroke-width="1.4">
            <circle cx="12" cy="12" r="7"/>
            <ellipse cx="12" cy="12" rx="3" ry="7"/>
            <path d="M5 12h14M6 8.5h12M6 15.5h12"/>
          </g>
        </svg>
      </li>
    </ul>
  </section>

</main>
</body>
</html>
```